Young Accounting firm needing a captivating business card

We need a business card design that forces the person to look at the card because its either gold foil, plastic, or lettering pop up etc. We already have a logo with a specific gold color and we need to make it pop. We are an accounting firm. I need the words" accounting, payroll, licenses, audits, taxes" somewhere on the business card so as to describe what we do- preferably on the side where the logo is at.

Industry/Entity Type

Accounting

Contact Information for Business Card

Address 48276 9th Ave S Ste 305, Cedar Hollow, OR 98117
Business Phone (360)418-2096
Fax (360)418-2157
Office Cell Phone (360)586-7319

Font styles to use
Serif

Colors
85abd2

Requirements
Must have
• It should state
• "Accounting" "Taxes" "Audits" "Licenses" "Payroll"
Nice to have
• Matte with gold foil, different textures, With Either a textured ivory background or gray blue slate background
Should not have
• colorful colors

```html
<!DOCTYPE html>
<html lang="en">
<head>
<meta charset="utf-8">
<title>Kestrel Ledger — Business Card</title>
<link rel="stylesheet" href="https://fonts.googleapis.com/css2?family=Montserrat:wght@400;500;600;700&display=swap">
<style>
  :root {
    --backdrop: #c9cbce;
    --card-dark: #2c2a29;
    --card-light: #fbfbfa;
    --gold: #c99a3c;
    --gold-deep: #a87a24;
    --gold-soft: #d8b467;
    --ink-light: #f1ece2;
  }
  * { box-sizing: border-box; margin: 0; padding: 0; }
  html, body {
    width: 1200px; height: 800px; overflow: hidden;
    background: var(--backdrop);
    font-family: "Montserrat", Arial, sans-serif;
  }
  .canvas {
    position: relative; width: 1200px; height: 800px;
    background: linear-gradient(160deg, #d9dadc 0%, #c3c5c8 55%, #b4b7ba 100%);
  }
  .card {
    position: absolute; left: 330px; width: 540px; height: 308px;
    box-shadow: 0 10px 24px rgba(0,0,0,0.22);
  }
  .card--front { top: 70px; background: var(--card-dark); }
  .card--back { top: 422px; background: var(--card-light); }

  /* front */
  .brand {
    position: absolute; left: 0; right: 0; top: 104px;
    display: flex; align-items: center; justify-content: center; gap: 12px;
  }
  .brand__mark { width: 34px; height: 34px; background: var(--gold); }
  .brand__name {
    font-size: 34px; font-weight: 500; color: var(--gold);
    letter-spacing: -0.5px;
  }
  .services {
    position: absolute; left: 0; right: 0; top: 196px;
    text-align: center; font-size: 13px; letter-spacing: 0.6px;
    color: var(--gold);
  }
  .services .first { color: var(--ink-light); }
  .services .sep { margin: 0 6px; color: var(--gold-soft); }

  /* back */
  .back-brand {
    position: absolute; left: 34px; top: 100px; width: 190px;
    display: flex; flex-direction: column; align-items: center; gap: 12px;
  }
  .back-brand__mark { width: 56px; height: 56px; background: var(--gold); }
  .back-brand__name { font-size: 22px; font-weight: 500; color: var(--gold); }
  .divider {
    position: absolute; left: 250px; top: 58px; width: 2px; height: 168px;
    background: linear-gradient(var(--gold-soft), var(--gold-deep));
  }
  .person { position: absolute; left: 276px; top: 58px; }
  .person__name { font-size: 20px; font-weight: 700; color: var(--gold); letter-spacing: 0.3px; }
  .person__title { font-size: 13px; font-weight: 500; color: var(--gold-soft); margin-top: 2px; }
  .contacts { list-style: none; margin-top: 14px; }
  .contacts li {
    display: flex; align-items: center; gap: 8px;
    font-size: 13.5px; font-weight: 500; color: var(--gold); line-height: 19px;
  }
  .contacts svg { width: 13px; height: 13px; flex: none; fill: none; stroke: var(--gold); stroke-width: 1.6; }
  .address {
    position: absolute; left: 34px; top: 262px;
    font-size: 14px; font-weight: 500; color: var(--gold);
  }
</style>
</head>
<body>
<main class="canvas">
  <section class="card card--front" aria-label="Card front">
    <div class="brand">
      <span class="brand__mark"></span>
      <span class="brand__name">Kestrel Ledger</span>
    </div>
    <p class="services">
      <span class="first">Accounting</span><span class="sep">|</span>Licenses<span class="sep">|</span>Audits<span class="sep">|</span>Taxes<span class="sep">|</span>Payroll
    </p>
  </section>

  <section class="card card--back" aria-label="Card back">
    <div class="back-brand">
      <span class="back-brand__mark"></span>
      <span class="back-brand__name">Kestrel Ledger</span>
    </div>
    <span class="divider"></span>
    <div class="person">
      <p class="person__name">Daniel Whitford</p>
      <p class="person__title">President</p>
      <ul class="contacts">
        <li><svg viewBox="0 0 16 16"><path d="M3 2h3l1 3-2 1.5a9 9 0 0 0 4.5 4.5L11 9l3 1v3a1 1 0 0 1-1 1A12 12 0 0 1 2 3a1 1 0 0 1 1-1z"/></svg>(360) 418-2096</li>
        <li><svg viewBox="0 0 16 16"><rect x="4" y="1.5" width="8" height="13" rx="1.2"/><path d="M7 12.3h2"/></svg>(360) 586-7319</li>
        <li><svg viewBox="0 0 16 16"><rect x="2" y="6" width="12" height="6" rx="1"/><path d="M4.5 6V2h7v4M4.5 10h7v4h-7z"/></svg>(360) 418-2157</li>
        <li><svg viewBox="0 0 16 16"><rect x="1.5" y="3.5" width="13" height="9"/><path d="M1.5 3.5 8 9l6.5-5.5"/></svg>daniel@kestrelledger.com</li>
        <li><svg viewBox="0 0 16 16"><circle cx="8" cy="8" r="6.3"/><path d="M1.7 8h12.6M8 1.7c-3 3.4-3 9.2 0 12.6M8 1.7c3 3.4 3 9.2 0 12.6"/></svg>www.kestrelledger.com</li>
      </ul>
    </div>
    <p class="address">48276 9th Ave S Ste 305, Cedar Hollow, OR 98117</p>
  </section>
</main>
</body>
</html>
```